Web Page Template and Logo Design

We are launching a website to sell homewares and would like a logo design, as well as a home page template, and the template for the product pages.

The homewares store is called Brassy Walrus. The homewares we will sell will be edgy and very bright colours. We envisage the theme of the homepage will have hot pink, some blue/ white chinioserie pattern and potentially lime green. We would like the logo to reflect humour and "Brassy Walrus".

The images uploaded reflect the look and feel of the type of people who are our customers - they are not minimalists and they are definitely not into beige!

Target Market(s)

Predominantly women, 30 - 50

Industry/Entity Type

Store

Number of Pages Required

2 page

Font styles to use
Sans Serif

Colors
e34197
acd036
33a6d7

Requirements
Must have
• Template for home page and standard template for other pages;PLEASE NOTE: I have now listed the Brassy Walrus Logo as a separate 2 day listing; a bright, bold, colourful website with a sense of humour (it needs to dare people to put something bright in their homes).
• Please Note: I don't need a whole website, I have one of my staff who can do that for me. I just want the creative template for the homepage and a standard template for the product pages. It is the graphic design and creative side I am more interested in. I will want my staff member to be able to take the design and incorporate it into the website.

```html
<!DOCTYPE html>
<html lang="en">
<head>
<meta charset="utf-8">
<title>Brassy Walrus – Home</title>
<link href="https://fonts.googleapis.com/css2?family=Open+Sans:wght@400;600&display=swap" rel="stylesheet">
<style>
:root{
  --pink:#e3148f;
  --pink-bg:#fbc6e3;
  --pink-bg-light:#fde3f1;
  --blue:#2d72d2;
  --link-blue:#3a7fc9;
  --quote-blue:#4a8fd8;
  --green:#79dd9a;
  --green-title:#5ccf85;
  --button-green:#a2e39a;
  --grey-text:#9a9a9a;
  --dark-text:#555;
  --line:#e2e2e2;
  --hero-grey:#eeeef0;
  --white:#fff;
}
*{box-sizing:border-box;margin:0;padding:0}
html,body{width:1017px;height:1200px;overflow:hidden}
body{
  font-family:"Open Sans",Arial,sans-serif;
  background:linear-gradient(135deg,var(--pink-bg-light),var(--pink-bg) 40%,var(--pink-bg-light) 70%,var(--pink-bg));
  position:relative;
}
.page{position:absolute;left:84px;top:0;width:849px;height:1200px;background:var(--white)}
.abs{position:absolute}
.brand{left:9px;top:16px;font-size:40px;color:var(--pink);font-weight:400;letter-spacing:-.5px}
.cart{right:12px;top:17px;font-size:13px;color:var(--pink);font-weight:600;display:flex;align-items:center;gap:5px}
.nav{right:12px;top:49px;display:flex;gap:23px;font-size:12px;color:var(--dark-text)}
.nav .active{color:#1ea7e0}
.hero{left:0;top:87px;width:849px;height:322px;background:var(--hero-grey)}
.hero-photo{position:absolute;left:0;top:0;width:479px;height:322px;background:linear-gradient(160deg,#f3a8cf,#e3469a 45%,#f6f2f4 78%,#e9e6e8)}
.quote{position:absolute;right:24px;top:84px;text-align:right;color:var(--quote-blue);font-size:21px;line-height:26.5px}
.btn-more{position:absolute;left:738px;top:174px;width:86px;height:33px;background:var(--button-green);color:#3c5a3c;font-size:11.5px;display:flex;align-items:center;justify-content:center;border-radius:2px}
.slider-arrows{position:absolute;left:792px;top:224px}
.welcome{left:0;top:439px;width:849px;text-align:center}
.welcome h1{font-weight:400;font-size:21px;color:var(--blue)}
.welcome p{margin:7px auto 0;width:775px;font-size:11.5px;line-height:19.5px;color:var(--grey-text)}
.divider{left:9px;top:575px;width:830px;height:1px;background:var(--line)}
.section-title{left:11px;top:606px;font-size:19.5px;color:var(--green-title);font-weight:400}
.more-arrow{left:667px;top:611px}
.card{width:184px;height:204px;border:1px solid var(--line);text-align:center}
.card .photo{margin:6px 6px 0;height:135px}
.card .name{margin-top:16px;font-size:11.5px;color:var(--link-blue)}
.card .basket{margin-top:5px}
.panel{left:618px;width:221px;border:1px solid var(--line)}
.panel h2{height:37px;background:var(--green);color:var(--white);font-weight:400;font-size:19.5px;line-height:37px;padding-left:10px;margin:-1px -1px 0}
.cat-list{list-style:none;padding:13px 0 0 16px}
.cat-list li{font-size:11.5px;color:var(--dark-text);line-height:26.5px;padding-left:14px;position:relative}
.cat-list li::before{content:"";position:absolute;left:0;top:12px;width:3px;height:3px;background:#888}
.newsletter p{font-size:10.5px;color:var(--dark-text);line-height:14px;padding:18px 15px 0}
.email{margin:20px 0 0 15px;width:193px;height:34px;border:1px solid var(--line);font-size:11px;color:var(--dark-text);padding:10px 15px;background:#fbfbfb}
.submit{margin:10px 0 0 150px;width:58px;height:30px;background:linear-gradient(#6a6a6a,#3c3c3c);color:var(--white);font-size:12px;display:flex;align-items:center;justify-content:center;border-radius:2px}
.footer-bar{left:21px;top:1107px;width:818px;height:5px;background:var(--line)}
.footer-links{left:24px;top:1133px;font-size:11.5px;color:var(--dark-text);display:flex;gap:9px}
.copyright{left:24px;top:1161px;font-size:11.5px;color:var(--dark-text)}
.social{left:736px;top:1143px;display:flex;gap:12px}
.social span{width:26px;height:26px;border-radius:50%;display:block}
</style>
</head>
<body>
<div class="page">
  <div class="abs brand">Brassy Walrus</div>
  <div class="abs cart">$00.00
    <svg width="14" height="11" viewBox="0 0 14 11"><path d="M1 4h12l-1.5 6.5h-9z" fill="var(--pink)"/><path d="M4 4l3-3 3 3" stroke="var(--pink)" fill="none" stroke-width="1.3"/></svg>
  </div>
  <nav class="abs nav"><span class="active">Home</span><span>About us</span><span>Products</span><span>Gallery</span><span>Contact us</span></nav>

  <section class="abs hero">
    <div class="hero-photo" role="img" aria-label="Photo of a white mantelpiece with a Venetian mirror, blue and white porcelain vases and pink flowers against a hot pink trellis wallpaper"></div>
    <div class="quote">If you dare nothing,<br>then when the day is over,<br>nothing is all you will have gained.</div>
    <div class="btn-more">VIEW MORE</div>
    <svg class="slider-arrows" width="33" height="21" viewBox="0 0 33 21"><circle cx="9" cy="10.5" r="9" fill="#aaa"/><circle cx="24" cy="10.5" r="9" fill="#aaa"/><path d="M11 6l-4 4.5 4 4.5M22 6l4 4.5-4 4.5" stroke="#fff" stroke-width="1.8" fill="none"/></svg>
  </section>

  <section class="abs welcome">
    <h1>Welcome to Brassy Walrus</h1>
    <p>Nullam faucibus orci id ligula facilisis lacinia. Vestibulum dui ex, feugiat sit amet ornare vel, interdum iaculis augue. Vestibulum suscipit eros non ex feugiat cursus. Proin quis imperdiet eros, sed mollis lorem. Sed a faucibus mi, sit amet fermentum ex. Maecenas congue mauris sed dolor mattis, sed rhoncus velit molestie. Donec mattis ex ut ante varius rhoncus. Pellentesque sit amet justo leo. Quisque pulvinar mollis convallis. Nunc convallis lectus nec est tristique, sollicitudin sagittis enim malesuada.</p>
  </section>
  <div class="abs divider"></div>

  <h2 class="abs section-title">Our Products</h2>
  <svg class="abs more-arrow" width="19" height="19" viewBox="0 0 19 19"><circle cx="9.5" cy="9.5" r="8.5" stroke="#999" fill="none" stroke-width="1.2"/><path d="M5 9.5h8M10 6.5l3 3-3 3" stroke="#999" fill="none" stroke-width="1.2"/></svg>

  <div class="abs card" style="left:11px;top:646px"><div class="photo" role="img" aria-label="Lime green chinoiserie cabinet filled with blue and white porcelain" style="background:linear-gradient(135deg,#b4d82c,#2f6a3a 50%,#b4d82c)"></div><div class="name">Product Name</div><svg class="basket" width="14" height="11" viewBox="0 0 14 11"><path d="M1 4h12l-1.5 6.5h-9z" fill="var(--link-blue)"/><path d="M4 4l3-3 3 3" stroke="var(--link-blue)" fill="none" stroke-width="1.3"/></svg></div>
  <div class="abs card" style="left:215px;top:646px"><div class="photo" role="img" aria-label="Colourful illustration of dancing figures in red and blue dresses" style="background:linear-gradient(135deg,#f4f1f1,#e05050 45%,#4a6fb0 75%,#f4f1f1)"></div><div class="name">Product Name</div><svg class="basket" width="14" height="11" viewBox="0 0 14 11"><path d="M1 4h12l-1.5 6.5h-9z" fill="var(--link-blue)"/><path d="M4 4l3-3 3 3" stroke="var(--link-blue)" fill="none" stroke-width="1.3"/></svg></div>
  <div class="abs card" style="left:418px;top:646px"><div class="photo" role="img" aria-label="Blue and white porcelain vase on patterned tiles" style="background:linear-gradient(135deg,#2a4c8c,#d8e0ee 50%,#3557a0)"></div><div class="name">Product Name</div><svg class="basket" width="14" height="11" viewBox="0 0 14 11"><path d="M1 4h12l-1.5 6.5h-9z" fill="var(--link-blue)"/><path d="M4 4l3-3 3 3" stroke="var(--link-blue)" fill="none" stroke-width="1.3"/></svg></div>
  <div class="abs card" style="left:11px;top:870px"><div class="photo" role="img" aria-label="Zebra figure standing in a bright white room" style="background:linear-gradient(135deg,#e8e8e6,#f4f4f2 50%,#5a5a5a)"></div><div class="name">Product Name</div><svg class="basket" width="14" height="11" viewBox="0 0 14 11"><path d="M1 4h12l-1.5 6.5h-9z" fill="var(--link-blue)"/><path d="M4 4l3-3 3 3" stroke="var(--link-blue)" fill="none" stroke-width="1.3"/></svg></div>
  <div class="abs card" style="left:215px;top:870px"><div class="photo" role="img" aria-label="Bright yellow wicker chair against a bold printed wall" style="background:linear-gradient(135deg,#e6e0e4,#f2e21a 55%,#d0486e)"></div><div class="name">Product Name</div><svg class="basket" width="14" height="11" viewBox="0 0 14 11"><path d="M1 4h12l-1.5 6.5h-9z" fill="var(--link-blue)"/><path d="M4 4l3-3 3 3" stroke="var(--link-blue)" fill="none" stroke-width="1.3"/></svg></div>
  <div class="abs card" style="left:418px;top:870px"><div class="photo" role="img" aria-label="Pink roses in a blue and white vase against pink trellis wallpaper" style="background:linear-gradient(160deg,#f2a6cc,#e3469a 50%,#2f4f9a)"></div><div class="name">Product Name</div><svg class="basket" width="14" height="11" viewBox="0 0 14 11"><path d="M1 4h12l-1.5 6.5h-9z" fill="var(--link-blue)"/><path d="M4 4l3-3 3 3" stroke="var(--link-blue)" fill="none" stroke-width="1.3"/></svg></div>

  <aside class="abs panel" style="top:605px;height:244px">
    <h2>Category</h2>
    <ul class="cat-list"><li>Aliquam ac pretium</li><li>Pellentesque sit</li><li>Quisque pulvinar</li><li>Nam eget erat</li><li>Nullam tincidunt</li><li>Nullam dictum diam</li><li>Sed sollicitudin</li></ul>
  </aside>
  <aside class="abs panel newsletter" style="top:871px;height:202px">
    <h2>Newsletter</h2>
    <p>Nullam dictum diam nec congue con sectetur mattis.</p>
    <div class="email">Email ID</div>
    <div class="submit">Submit</div>
  </aside>

  <div class="abs footer-bar"></div>
  <nav class="abs footer-links"><span>Home</span><span>|</span><span>About us</span><span>|</span><span>Products</span><span>|</span><span>Gallery</span><span>|</span><span>Contact us</span></nav>
  <div class="abs copyright">Copyright &nbsp;©&nbsp; 2014 &nbsp; Brassy Walrus. &nbsp; All rights reserved.</div>
  <div class="abs social" role="img" aria-label="Social media links"><span style="background:#3b5ba0"></span><span style="background:#2aa6e8"></span><span style="background:#1a8cc0"></span></div>
</div>
</body>
</html>
```